Computer business needs new look.

KELD Computers has been selling and repairing, servicing computers in northern NSW for 20 years and has now branched out into Surveillance/ CCTV systems Alarm systems and just about anything technical.
We have also changed our area of operation from just the northern rivers to include all of outback New South Wales and Queensland.
We have changed our name slightly to K.E.L.D Sundown Technical Services.I will include my old business card.The Logo can stay or go i am open to all designs.
Updates

facebook page for info https://www.examplebook.test/pages/KELD-Computers/482019375610283?fref=ts The top half of the business card i uploaded looks pink ! it should be white

I should have mentioned this before. My new look cards will become the look of the business. ie: advertising, vehicle sign-writing etc: The look that i think im after is more to large business/corporate look not "WALLY THE FIXER " Probably the main focus is the fact that we service the small towns in outback Australia. " Billabong Barney " Not just the big city's Please feel free to through any thing at me and any questions please ask.

I have uploaded a picture that i would like the back of the card to look like. Please have a look and see what you can do.

Reason: I am hoping to get some original designs that i like. So far i have just 1 that i like..there must be more ideas out there.

Target Market(s)

Small to medium business

Industry/Entity Type

Business

Contact Information for Business Card

K.E.L.D Sundown Technical Services
Owen Pelkie
1300621745 0457 318206

Requirements
Nice to have
• Back of card to have a list of services
Computer sales
Computer Repairs & Virus removal
Wireless Hotspots
CCTV Installation and repair
Network Design and setup
Troubleshooting

```html
<!DOCTYPE html>
<html lang="en">
<head>
<meta charset="utf-8">
<title>K.E.L.D Sundown Technical Services – Business Card</title>
<link rel="stylesheet" href="https://fonts.googleapis.com/css2?family=Open+Sans:wght@300;400;600;700&display=swap">
<style>
  :root {
    --stage: #e9ebee;
    --blue-deep: #0b5aa8;
    --blue-mid: #1378cc;
    --blue-light: #2a93e0;
    --white: #ffffff;
    --paper: #f4f5f6;
    --grey-band: #8a8d91;
    --grey-text: #5b5e62;
    --divider: rgba(255,255,255,0.55);
  }
  * { box-sizing: border-box; margin: 0; padding: 0; }
  html, body {
    width: 1200px; height: 900px; overflow: hidden;
    background: var(--stage);
    font-family: "Open Sans", Arial, sans-serif;
  }
  .canvas {
    position: relative; width: 1200px; height: 900px;
  }
  .card {
    position: absolute; left: 320px; width: 560px; height: 320px;
    overflow: hidden; border-radius: 3px;
    box-shadow: 0 10px 30px rgba(0,0,0,0.18);
  }

  /* Back of card */
  .card-back {
    top: 100px;
    background: linear-gradient(120deg, var(--blue-light) 0%, var(--blue-mid) 45%, var(--blue-deep) 100%);
    color: var(--white);
  }
  .card-back .mark {
    position: absolute; left: 30px; top: 108px;
    display: flex; align-items: center; gap: 14px;
  }
  .card-back .mark-dot {
    width: 104px; height: 104px; border-radius: 50%;
    background: var(--white); flex: none;
  }
  .card-back .mark-name {
    font-weight: 700; font-size: 50px; line-height: 1; letter-spacing: 2px; color: var(--white);
  }
  .card-back .divider {
    position: absolute; left: 330px; top: 52px; width: 1px; height: 216px;
    background: var(--divider);
  }
  .services {
    position: absolute; left: 344px; top: 66px;
    list-style: none; font-size: 12.5px; line-height: 26px; font-weight: 400;
    white-space: nowrap;
  }
  .services li:nth-child(2) { padding-left: 4px; }
  .services li:nth-child(3) { padding-left: 8px; }
  .services li:nth-child(4) { padding-left: 12px; }
  .services li:nth-child(5) { padding-left: 16px; }
  .services li:nth-child(6) { padding-left: 20px; }
  .services li:nth-child(7) { padding-left: 24px; }

  /* Front of card */
  .card-front {
    top: 480px; background: var(--paper);
  }
  .card-front .mark {
    position: absolute; left: 30px; top: 52px;
    display: flex; align-items: center; gap: 10px;
  }
  .card-front .mark-dot {
    width: 58px; height: 58px; border-radius: 50%;
    background: var(--blue-mid); flex: none;
  }
  .card-front .mark-name {
    font-weight: 700; font-size: 34px; color: var(--blue-deep); letter-spacing: 1px;
  }
  .company-name {
    position: absolute; left: 200px; top: 60px;
    font-size: 16px; font-weight: 600; line-height: 19px;
    letter-spacing: 1.5px; color: var(--grey-text); text-transform: uppercase;
    white-space: nowrap;
  }
  .grey-band {
    position: absolute; left: 0; top: 150px; width: 100%; height: 8px;
    background: var(--grey-band);
  }
  .blue-panel {
    position: absolute; left: 0; top: 166px; width: 100%; height: 154px;
    background: linear-gradient(100deg, var(--blue-light) 0%, var(--blue-mid) 50%, var(--blue-deep) 100%);
    color: var(--white);
  }
  .person-name {
    position: absolute; left: 30px; top: 46px;
    font-size: 30px; font-weight: 400; white-space: nowrap;
  }
  .person-email {
    position: absolute; left: 32px; top: 96px; font-size: 14px; font-weight: 300;
  }
  .contact {
    position: absolute; left: 300px; top: 30px;
    font-size: 13.5px; line-height: 22px; font-weight: 400; white-space: nowrap;
  }
</style>
</head>
<body>
<main class="canvas">

  <section class="card card-back" aria-label="Back of business card">
    <div class="mark">
      <span class="mark-dot"></span>
      <span class="mark-name">KELD</span>
    </div>
    <span class="divider"></span>
    <ul class="services">
      <li>- Computer sales</li>
      <li>- Computer Repairs</li>
      <li>- Virus removal</li>
      <li>- CCTV Installation and repair</li>
      <li>- Alarm Installation</li>
      <li>- Network Design and setup</li>
      <li>- Printer Sales and Setup</li>
    </ul>
  </section>

  <section class="card card-front" aria-label="Front of business card">
    <div class="mark">
      <span class="mark-dot"></span>
      <span class="mark-name">KELD</span>
    </div>
    <p class="company-name">Kestrel East Link<br>Digital</p>
    <span class="grey-band"></span>
    <div class="blue-panel">
      <p class="person-name">Owen Pelkie</p>
      <p class="person-email">owen@keld.com.au</p>
      <p class="contact">
        K.E.L.D Sundown Technical Services<br>
        P: 1300621745 M: 0457 318206<br>
        www.keld.example
      </p>
    </div>
  </section>

</main>
</body>
</html>
```